Design Cloud for Core Values & Attributes

See Image Example Below "Word Cloud" this is what we would like this to look like.
The second image is all of the Core Value and Attributes I will list below.
CORE VALUES need to be the bigger words (based off the image I sent) Capitalized, BOLD, Navy
Independence, Capitalism, Trust, Fun, Safety, Growth
ATTRIBUTES need to be the smaller words, lower case, non-bold, lighter blue mixed in (based off the image I sent):
Humility, Consistency, Open Mindedness, Curiosity, Selflessness, Caring, Conscientiousness, Honorable, Cunning, Competitive, Compartmentalization, Innovative, Perseverance, Authenticity, Decisiveness, Self-efficacy, Accountability, Generosity, Humor, Optimism, Resilience, Inclusive, Insouciance to what others think, Courage, Decisive, Curious, Integrity

```html
<!DOCTYPE html>
<html lang="en">
<head>
<meta charset="utf-8">
<title>Core Values Word Cloud</title>
<link rel="stylesheet" href="https://fonts.googleapis.com/css2?family=Poppins:wght@300;400;700;800&display=swap">
<style>
  :root {
    --page: #e8f3fb;
    --card-light: #ffffff;
    --card-shade: #e6e6e6;
    --swoosh: #ffffff;
    --navy-top: #0056ab;
    --navy-bottom: #07458b;
    --attribute: #5ca4d2;
    --value-dark: #222222;
  }
  html, body {
    margin: 0;
    width: 1200px;
    height: 1200px;
    overflow: hidden;
    background: var(--page);
  }
  .design {
    position: absolute;
    left: 0;
    top: 200px;
    width: 1200px;
    height: 800px;
    display: block;
  }
  .headline {
    font-family: "Poppins", sans-serif;
    font-weight: 800;
    font-size: 158px;
  }
  .attribute {
    font-family: "Poppins", sans-serif;
    font-weight: 300;
    font-size: 29px;
    fill: var(--attribute);
  }
  .attribute-strong {
    font-family: "Poppins", sans-serif;
    font-weight: 700;
    font-size: 44px;
    fill: var(--attribute);
  }
  .value {
    font-family: "Poppins", sans-serif;
    font-weight: 700;
    font-size: 30px;
    fill: var(--value-dark);
  }
  .end { text-anchor: end; }
  .swoosh { fill: none; stroke: var(--swoosh); stroke-width: 1.5; opacity: .9; }
  .swoosh-band { fill: var(--swoosh); opacity: .55; }
</style>
</head>
<body>
<svg class="design" viewBox="0 0 1200 800" xmlns="http://www.w3.org/2000/svg">
  <defs>
    <radialGradient id="card-fill" cx="50%" cy="45%" r="75%">
      <stop offset="0" stop-color="var(--card-light)"/>
      <stop offset="0.7" stop-color="#f4f4f4"/>
      <stop offset="1" stop-color="var(--card-shade)"/>
    </radialGradient>
    <linearGradient id="core-fill" gradientUnits="userSpaceOnUse" x1="0" y1="276" x2="0" y2="386">
      <stop offset="0.46" stop-color="var(--navy-top)"/>
      <stop offset="0.46" stop-color="var(--navy-bottom)"/>
    </linearGradient>
    <linearGradient id="values-fill" gradientUnits="userSpaceOnUse" x1="0" y1="399" x2="0" y2="510">
      <stop offset="0.5" stop-color="var(--navy-top)"/>
      <stop offset="0.5" stop-color="var(--navy-bottom)"/>
    </linearGradient>
  </defs>

  <rect width="1200" height="800" fill="url(#card-fill)"/>
  <path class="swoosh-band" d="M0 575 C 260 640 520 700 1200 660 L1200 800 L0 800 Z"/>
  <path class="swoosh" d="M0 385 C 180 560 520 640 1200 360"/>
  <path class="swoosh" d="M0 240 C 240 420 700 520 1200 300"/>
  <path class="swoosh" d="M1030 0 C 960 260 860 520 720 800"/>
  <path class="swoosh" d="M1120 0 C 1060 300 980 560 880 800"/>

  <!-- Headline -->
  <text class="headline" x="307" y="386" textLength="413" lengthAdjust="spacingAndGlyphs" fill="url(#core-fill)">CORE</text>
  <text class="headline" x="307" y="510" textLength="593" lengthAdjust="spacingAndGlyphs" fill="url(#values-fill)">VALUES</text>

  <!-- Upper cluster -->
  <text class="attribute-strong" transform="translate(226 256) rotate(-90)" textLength="187" lengthAdjust="spacingAndGlyphs">HUMILITY</text>
  <text class="attribute" x="245" y="92" textLength="436" lengthAdjust="spacingAndGlyphs">Honorable Conscientiousness</text>
  <text class="attribute" x="245" y="131">Cunning</text>
  <text class="attribute" x="400" y="131">Perseverance</text>
  <text class="attribute" x="245" y="171">Selflessness</text>
  <text class="attribute" x="449" y="171">Innovative</text>
  <text class="attribute" x="245" y="210">Curiosity</text>
  <text class="attribute" x="400" y="210">Competitive</text>
  <text class="attribute-strong" x="237" y="256" textLength="383" lengthAdjust="spacingAndGlyphs">OPEN MINDEDNESS</text>
  <text class="attribute" transform="translate(638 208) rotate(-90)">Humor</text>
  <text class="attribute" transform="translate(675 256) rotate(-90)">Generosity</text>
  <text class="attribute" transform="translate(712 256) rotate(-90)">Authenticity</text>

  <text class="value" transform="translate(760 258) rotate(-90)" textLength="94" lengthAdjust="spacingAndGlyphs">TRUST</text>
  <text class="attribute" x="772" y="171">Self-efficacy</text>
  <text class="attribute" x="772" y="213">Decisiveness</text>
  <text class="attribute" x="772" y="256">Compartmentalization</text>

  <!-- Left cluster -->
  <text class="value end" x="290" y="297">TRUST</text>
  <text class="attribute end" x="290" y="337">Resilience</text>
  <text class="attribute end" x="290" y="372">Inclusive</text>
  <text class="value end" x="290" y="422">FUN</text>
  <text class="attribute end" x="259" y="456">Integrity</text>
  <text class="attribute end" x="259" y="502">Humor</text>
  <text class="attribute end" x="259" y="544">Curiosity</text>
  <text class="attribute" transform="translate(290 707) rotate(-90)" textLength="272" lengthAdjust="spacingAndGlyphs">Conscientiousness</text>

  <!-- Right cluster -->
  <text class="value" x="737" y="297" textLength="231" lengthAdjust="spacingAndGlyphs">INDEPENDENCE</text>
  <text class="attribute" x="737" y="337">Accountability</text>
  <text class="attribute" x="737" y="372">Optimism</text>
  <text class="attribute" x="902" y="372">Resilience</text>
  <text class="attribute" x="916" y="428">Cunning</text>
  <text class="attribute" x="916" y="468">Selflessness</text>
  <text class="attribute" x="916" y="505">Curiosity</text>

  <!-- Lower cluster -->
  <text class="attribute" x="326" y="546">Insouciance to what</text>
  <text class="attribute" x="326" y="571">others think</text>
  <text class="value end" x="859" y="546">GROWTH</text>
  <text class="attribute" x="531" y="577">Innovative</text>
  <text class="attribute" x="700" y="577">Curious</text>
  <text class="attribute" x="326" y="616">Courage</text>
  <text class="attribute" x="477" y="616">Innovative</text>
  <text class="attribute" x="658" y="616">Innovative</text>
  <text class="attribute" x="326" y="662">Decisive</text>
  <text class="attribute" x="477" y="662">Perseverance</text>
  <text class="attribute end" x="811" y="662">Humor</text>
  <text class="attribute" x="326" y="703">Cunning</text>
  <text class="attribute" x="477" y="703">Selflessness</text>
  <text class="attribute" x="659" y="703">Innovative</text>
  <text class="attribute-strong" transform="translate(859 710) rotate(-90)" textLength="155" lengthAdjust="spacingAndGlyphs">CARING</text>
  <text class="value" transform="translate(876 523) rotate(90)" textLength="184" lengthAdjust="spacingAndGlyphs">CAPITALISM</text>
</svg>
</body>
</html>
```